Premium website for 'Kestrel Voyages Elite'

Exclusive Torque League travel packages: world-class tickets, premium hospitality, seamless travel, and curated experiences that bring the spirit of each destination to life.

1. Overall Style and Impression
Aesthetic: Modern, premium, and dynamic, reflecting the speed and excitement of a high-profile sport or event.

Focus: Highly visual and focused on driving users toward specific, high-value conversion points (like finding a race or viewing a premium package).

We need on the homepage a few blocks for all destinations.
One the specific page of the destination, we need a list of tickets.
An example for our website is https://zomerratours.com/

Functional requirements

The web site is designed to deliver an end-to-end Torque League travel experience, combining flight bookings, hotel reservations, and race ticket purchases into one seamless booking process. This system provides a unified API layer that integrates external booking services and enables developers to build, manage, and customize complete travel packages for each TL Grand Prix event.

System Overview

The platform is built around three core microservices, all connected through a central Package API:

1. Flight Booking Service ✈️
Integrates with global flight providers (e.g.,Flyvora API).

2. Hotel Booking Service 🏨
Connects to hotel aggregator APIs (e.g., Bunkly).
Offers real-time availability, dynamic pricing, and filtering by proximity to TL circuits.

3. Ticket Booking Service 🎟️
Manages TL race ticket inventory and seat categories (Grandstand, VIP, General Admission).

CUSTOMER FEEDBACK
After each booking, a customer will be asked to fill in a questionaire.

CHAT BOT
A chat bot will answer the frequently asked questions.

OUR VISION
We believe life is meant to be lived at full throttle.
Not just seen, but felt. Not just remembered, but relived again and again.

MISSION
That’s why we craft once-in-a-lifetime Torque League journeys — where the roar of the engines meets the soul of the city. Where luxury travel and local culture collide with pure adrenaline. Where you don’t just watch the race… you become part of its story.

PRODUCTS

Target Market(s)

Affluent individuals, typically 35−65 years old, in professional, executive, or entrepreneurial roles. High net worth with significant disposable income.

Coding

Coded - Design and coding required

Number of Pages Required

5+ page

Requirements
Must have
• Central Package API
Nice to have
• Customer feedback after each booking , chat bot.

```html
<!DOCTYPE html>
<html lang="en">
<head>
<meta charset="utf-8">
<title>Kestrel Voyages Elite — Torque League Travel Packages</title>
<link href="https://fonts.googleapis.com/css2?family=Roboto:ital,wght@0,300;0,400;0,500;0,700;0,900;1,400&display=swap" rel="stylesheet">
<style>
:root{
  --ink:#111111;
  --ink-2:#1b1b1b;
  --yellow:#ffd800;
  --white:#ffffff;
  --text:#222222;
  --muted:#555555;
  --line:#d6d6d6;
  --footer-text:#b9b9b9;
}
*{box-sizing:border-box;margin:0;padding:0}
html,body{width:1200px;height:3251px;overflow:hidden}
body{font-family:'Roboto',sans-serif;color:var(--text);background:var(--white)}
.wrap{width:928px;margin:0 auto;position:relative}

/* top bar */
.topbar{height:44px;background:var(--ink);position:relative}
.topbar .wrap{display:flex;align-items:center;height:44px;gap:44px}
.topbar .contact{display:flex;align-items:center;gap:10px;color:var(--yellow);font-size:13px}
.topbar .account{position:absolute;right:0;top:0;width:272px;height:44px;background:var(--yellow);
  clip-path:polygon(22px 0,100% 0,100% 100%,0 100%);display:flex;align-items:center;gap:34px;padding-left:40px}

/* nav */
.nav{height:67px;background:var(--ink)}
.nav .wrap{display:flex;align-items:center;justify-content:space-between;height:67px}
.brand{display:flex;align-items:center;gap:9px;color:var(--white);font-weight:700;font-size:21px;text-transform:uppercase;letter-spacing:.2px;white-space:nowrap}
.brand .mark{width:14px;height:14px;background:var(--yellow);flex:none}
.nav ul{display:flex;list-style:none;gap:25px}
.nav a{color:var(--white);font-size:13px;text-decoration:none}

/* hero */
.hero{height:300px;position:relative;
  background:radial-gradient(ellipse at 75% 45%,#4a4c52 0%,#2a2b30 35%,#141416 75%),#141416}
.hero .wrap{padding-top:82px}
.hero h1{color:var(--white);font-size:39px;font-weight:900;text-transform:uppercase;letter-spacing:.3px;line-height:46px}
.hero p{color:var(--yellow);font-size:19px;line-height:33px;margin-top:14px;width:600px}
.band{height:29px;background:var(--yellow)}

/* blocks */
.block{padding-top:56px}
.block h2{text-align:center;font-size:34px;font-weight:900;text-transform:uppercase;line-height:40px;color:var(--ink)}
.block h2::after{content:"";display:block;width:130px;height:4px;background:var(--yellow);margin:6px auto 0}
.row-head{display:flex;justify-content:space-between;align-items:center;height:40px;margin-top:33px}
.view-all{display:flex;align-items:center;gap:16px;font-size:26px;font-weight:700;color:var(--ink)}
.pager{display:flex;gap:2px}
.pager span{width:32px;height:44px;display:flex;align-items:center;justify-content:center;background:#eeeeee;border:1px solid #cfcfcf}
.pager span:first-child{background:#bdbdbd}
.cards{display:flex;gap:17px;margin-top:35px}
.photo{display:block;height:174px;width:100%}

/* ticket cards */
.ticket{width:298px;height:362px;background:var(--ink);padding:8px;text-align:center}
.ticket .date{color:var(--white);font-size:11px;margin-top:18px}
.ticket h3{color:var(--white);font-size:20px;font-weight:500;margin-top:9px;white-space:nowrap}
.ticket .venue{color:var(--yellow);font-size:14px;margin-top:9px;text-transform:uppercase;white-space:nowrap}
.ticket .cta{display:block;margin:16px 10px 0;height:44px;line-height:44px;background:var(--yellow);color:var(--ink);font-weight:700;font-size:16px}

/* package cards */
.package{width:298px;height:408px;padding:8px 8px 0;position:relative}
.package.light{background:var(--white);border:1px solid #d4d4d4;box-shadow:0 1px 4px rgba(0,0,0,.18)}
.package.dark{background:var(--ink)}
.package h3{font-size:20px;font-weight:500;margin:18px 0 0 8px;white-space:nowrap}
.package.light h3{color:var(--ink)}
.package.dark h3{color:var(--yellow);font-weight:700}
.package p{font-size:12px;line-height:20px;text-align:justify;margin:14px 8px 0;font-weight:300}
.package.light p{color:var(--muted)}
.package.dark p{color:var(--white)}
.btn{position:absolute;left:17px;bottom:19px;width:134px;height:45px;line-height:45px;text-align:center;background:var(--yellow);color:var(--ink);font-size:14px;font-weight:500;text-transform:uppercase}

/* curated */
.curated{background:var(--yellow);height:625px;padding-top:61px}
.curated h2{text-align:center;font-size:34px;font-weight:900;text-transform:uppercase;line-height:40px;color:var(--ink)}
.curated h2::after{content:"";display:block;width:130px;height:4px;background:var(--white);margin:6px auto 0}
.reviews{display:flex;gap:19px;margin:38px 0 0 -2px;width:932px}
.review{width:457px;height:350px;background:var(--white);border:1px solid #cfcfcf;text-align:center;padding-top:18px}
.avatar{width:92px;height:90px;margin:0 auto;background:linear-gradient(#e9ece9,#c9cfc9);border:1px solid #bbb}
.review h4{font-size:20px;font-weight:500;margin-top:15px;color:var(--ink)}
.review .place{font-size:12px;font-style:italic;color:var(--muted);margin-top:8px}
.review p{font-size:15px;line-height:24px;color:#333;margin:18px 24px 0}
.dots{display:flex;justify-content:center;gap:18px;margin-top:42px}
.dots span{width:37px;height:9px;background:var(--white)}
.dots span.on{background:var(--ink)}

/* footer */
.footer{background:var(--ink);height:237px;position:relative;padding-top:41px}
.footer .cols{display:flex}
.footer .col{width:228px}
.footer .col.contact-col{width:244px}
.footer h5{color:var(--white);font-size:17px;font-weight:700;text-transform:uppercase;margin-bottom:13px}
.footer li{list-style:none;color:var(--footer-text);font-size:15px;font-weight:300;line-height:27px;white-space:nowrap}
.footer .brand{font-size:17px;margin:7px 0 10px}
.legal{position:absolute;left:0;right:0;bottom:0;height:32px;border-top:1px solid #2a2a2a}
.legal .wrap{display:flex;gap:18px;font-size:12px;color:#888;line-height:30px}
.chat{position:absolute;left:1063px;top:123px;width:102px;height:38px;background:var(--yellow);display:flex;align-items:center;justify-content:center;gap:8px;font-weight:700;font-size:19px;color:var(--ink)}
</style>
</head>
<body>

<header>
  <div class="topbar">
    <div class="wrap">
      <div class="contact">
        <svg width="15" height="15" viewBox="0 0 24 24" fill="#ffd800"><path d="M6.6 10.8a15 15 0 0 0 6.6 6.6l2.2-2.2a1 1 0 0 1 1-.25 11.4 11.4 0 0 0 3.6.57 1 1 0 0 1 1 1V20a1 1 0 0 1-1 1A17 17 0 0 1 3 4a1 1 0 0 1 1-1h3.5a1 1 0 0 1 1 1c0 1.25.2 2.45.57 3.57a1 1 0 0 1-.25 1z"/></svg>
        +1 555 0142 880
      </div>
      <div class="contact">
        <svg width="17" height="14" viewBox="0 0 24 18" fill="none" stroke="#ffd800" stroke-width="2"><rect x="1" y="1" width="22" height="16"/><path d="M1 1l11 9 11-9"/></svg>
        hello@kestrelvoyages.example
      </div>
      <div class="account">
        <svg width="24" height="26" viewBox="0 0 24 26" fill="none" stroke="#111" stroke-width="1.8"><circle cx="12" cy="8" r="6"/><path d="M1 25c1-6 5-9 11-9s10 3 11 9"/></svg>
        <svg width="22" height="26" viewBox="0 0 22 26" fill="none" stroke="#111" stroke-width="1.8"><rect x="2" y="8" width="18" height="17"/><path d="M7 11V5a4 4 0 0 1 8 0v6"/></svg>
      </div>
    </div>
  </div>
  <nav class="nav">
    <div class="wrap">
      <div class="brand"><span class="mark"></span>Kestrel Voyages Elite</div>
      <ul>
        <li><a href="#">Home</a></li>
        <li><a href="#">World class tickets</a></li>
        <li><a href="#">Premium Hospitality</a></li>
        <li><a href="#">Seamless Travel</a></li>
        <li><a href="#">Curated</a></li>
      </ul>
    </div>
  </nav>
</header>

<section class="hero" role="img" aria-label="Race car speeding along a track with motion blur">
  <div class="wrap">
    <h1>Products of all travel packages</h1>
    <p>world-class tickets, premium hospitality, seamless travel, and curated experiences that bring the spirit of each destination to life.</p>
  </div>
</section>
<div class="band"></div>

<section class="block" style="height:593px">
  <div class="wrap">
    <h2>Torque League World-Class Tickets</h2>
    <div class="row-head">
      <div class="view-all">View All
        <svg width="40" height="12" viewBox="0 0 40 12" fill="none" stroke="#111" stroke-width="1.6"><path d="M0 6h38M32 1l6 5-6 5"/></svg></div>
      <div class="pager">
        <span><svg width="8" height="12" viewBox="0 0 8 12" fill="none" stroke="#111" stroke-width="1.6"><path d="M7 1L2 6l5 5"/></svg></span>
        <span><svg width="8" height="12" viewBox="0 0 8 12" fill="none" stroke="#111" stroke-width="1.6"><path d="M1 1l5 5-5 5"/></svg></span>
      </div>
    </div>
    <div class="cards">
      <article class="ticket">
        <span class="photo" role="img" aria-label="Red race car on a sunlit circuit straight" style="background:linear-gradient(180deg,#5d7fa8 0%,#9aa6b2 45%,#6b4a45 70%,#3a3a3e 100%)"></span>
        <div class="date">12 - 14 DECEMBER 2025</div>
        <h3>2025 Dunehaven Grand Prix</h3>
        <div class="venue">Dunehaven International Circuit</div>
        <div class="cta">ON SALE NOW</div>
      </article>
      <article class="ticket">
        <span class="photo" role="img" aria-label="Race car on a neon-lit city street at night" style="background:linear-gradient(180deg,#2c3a52 0%,#6d5a4a 40%,#a2673b 60%,#2b2c33 100%)"></span>
        <div class="date">05 - 07 DECEMBER 2025</div>
        <h3>2025 Neon City Grand Prix</h3>
        <div class="venue">Neon Boulevard Circuit</div>
        <div class="cta">ON SALE NOW</div>
      </article>
      <article class="ticket">
        <span class="photo" role="img" aria-label="Two race cars battling wheel to wheel" style="background:linear-gradient(180deg,#7a3a22 0%,#c26a3a 35%,#6e6660 65%,#2d2d30 100%)"></span>
        <div class="date">14 - 16 NOVEMBER 2025</div>
        <h3>2025 Serra Alta Grand Prix</h3>
        <div class="venue">Autódromo Serra Alta</div>
        <div class="cta">ON SALE NOW</div>
      </article>
    </div>
  </div>
</section>

<section class="block" style="height:648px">
  <div class="wrap">
    <h2>Premium Hospitality</h2>
    <div class="row-head" style="margin-top:35px">
      <div class="view-all">View All
        <svg width="40" height="12" viewBox="0 0 40 12" fill="none" stroke="#111" stroke-width="1.6"><path d="M0 6h38M32 1l6 5-6 5"/></svg></div>
      <div class="pager">
        <span><svg width="8" height="12" viewBox="0 0 8 12" fill="none" stroke="#111" stroke-width="1.6"><path d="M7 1L2 6l5 5"/></svg></span>
        <span><svg width="8" height="12" viewBox="0 0 8 12" fill="none" stroke="#111" stroke-width="1.6"><path d="M1 1l5 5-5 5"/></svg></span>
      </div>
    </div>
    <div class="cards" style="margin-top:39px">
      <article class="package light">
        <span class="photo" role="img" aria-label="Illuminated hotel facade sign at dusk" style="background:linear-gradient(135deg,#5a1a1e 0%,#a0582e 45%,#d9a25a 70%,#6e4a34 100%)"></span>
        <h3>Aurel Hotels of Lasvegas</h3>
        <p>Secure general admission, premium grandstand or all-inclusive hospitality tickets at Neon Boulevard Circuit, for excellent viewing of the action throughout the weekend.</p>
        <div class="btn">Book Now</div>
      </article>
      <article class="package light">
        <span class="photo" role="img" aria-label="Hotel sign with stars framed by palm trees at sunset" style="background:linear-gradient(180deg,#e0a24a 0%,#b35a2e 45%,#7a2a24 65%,#3b2a22 100%)"></span>
        <h3>Aurel Hotels of Florida</h3>
        <p>Upgrade your access in Neon City with TL Experiences! Ticket Package includes access to excellent trackside seating, premium hospitality and exclusive insider activities.</p>
        <div class="btn">Book Now</div>
      </article>
      <article class="package light">
        <span class="photo" role="img" aria-label="Modern hotel building with landscaped entrance" style="background:linear-gradient(180deg,#8fb3d4 0%,#c8cdd2 40%,#8a8f88 70%,#3f5a38 100%)"></span>
        <h3>Aurel Hotels of Nevada</h3>
        <p>Upgrade your access in Neon City with TL Experiences! Ticket Package includes access to excellent trackside seating, premium hospitality and exclusive insider activities.</p>
        <div class="btn">Book Now</div>
      </article>
    </div>
  </div>
</section>

<section class="block" style="height:708px">
  <div class="wrap">
    <h2>Seamless Travel</h2>
    <div class="row-head" style="margin-top:35px">
      <div class="view-all">View All
        <svg width="40" height="12" viewBox="0 0 40 12" fill="none" stroke="#111" stroke-width="1.6"><path d="M0 6h38M32 1l6 5-6 5"/></svg></div>
      <div class="pager">
        <span><svg width="8" height="12" viewBox="0 0 8 12" fill="none" stroke="#111" stroke-width="1.6"><path d="M7 1L2 6l5 5"/></svg></span>
        <span><svg width="8" height="12" viewBox="0 0 8 12" fill="none" stroke="#111" stroke-width="1.6"><path d="M1 1l5 5-5 5"/></svg></span>
      </div>
    </div>
    <div class="cards" style="margin-top:39px">
      <article class="package dark">
        <span class="photo" role="img" aria-label="Coach bus on a country road at sunset" style="background:linear-gradient(180deg,#5f7c9a 0%,#e7c06a 40%,#6f7a3a 65%,#3a3d36 100%)"></span>
        <h3>Bus Seamless Travel</h3>
        <p>Secure general admission, premium grandstand or all-inclusive hospitality tickets at Neon Boulevard Circuit, for excellent viewing of the action throughout the weekend.</p>
        <div class="btn">Book Now</div>
      </article>
      <article class="package dark">
        <span class="photo" role="img" aria-label="Passenger jet flying against a blue sky" style="background:linear-gradient(180deg,#1f6fc4 0%,#3a8fdc 55%,#7ab6ea 100%)"></span>
        <h3>Flight Seamless Travel</h3>
        <p>Upgrade your access in Neon City with TL Experiences! Ticket Package includes access to excellent trackside seating, premium hospitality and exclusive insider activities.</p>
        <div class="btn">Book Now</div>
      </article>
      <article class="package dark">
        <span class="photo" role="img" aria-label="Red high-speed train at a station platform at dawn" style="background:linear-gradient(180deg,#c9c2b5 0%,#e3a46a 35%,#a8322e 60%,#4a4a4e 100%)"></span>
        <h3>Train Seamless Travel</h3>
        <p>Upgrade your access in Neon City with TL Experiences! Ticket Package includes access to excellent trackside seating, premium hospitality and exclusive insider activities.</p>
        <div class="btn">Book Now</div>
      </article>
    </div>
  </div>
</section>

<section class="curated">
  <div class="wrap">
    <h2>Curated Experiences</h2>
    <div class="reviews">
      <article class="review">
        <div class="avatar" role="img" aria-label="Customer portrait"></div>
        <h4>Marlo Vance</h4>
        <div class="place">California, USA</div>
        <p>Lorem ipsum dolor sit amet, consectetur adipiscing elit, sed do eiusmod tempor incididunt ut labore et dolore magna aliqua. Ut enim ad minim veniam, quis nostrud exercitation ullamco laboris nisi ut aliquip ex ea commodo consequat. Duis aute irure dolor in reprehenderit in voluptate velit esse cillum dolore eu fugiat nulla pariatur.</p>
      </article>
      <article class="review">
        <div class="avatar" role="img" aria-label="Customer portrait"></div>
        <h4>Elise Harrow</h4>
        <div class="place">Florida, USA</div>
        <p>Lorem ipsum dolor sit amet, consectetur adipiscing elit, sed do eiusmod tempor incididunt ut labore et dolore magna aliqua. Ut enim ad minim veniam, quis nostrud exercitation ullamco laboris nisi ut aliquip ex ea commodo consequat. Duis aute irure dolor in reprehenderit in voluptate velit esse cillum dolore eu fugiat nulla pariatur.</p>
      </article>
    </div>
    <div class="dots"><span></span><span class="on"></span><span></span></div>
  </div>
</section>

<footer class="footer">
  <div class="wrap">
    <div class="cols">
      <div class="col">
        <h5>Buy TL Tickets</h5>
        <ul><li>World Class Tickets</li><li>Premium Hospitality</li><li>Seamless Travel</li><li>Curated Experiences</li></ul>
      </div>
      <div class="col">
        <h5>Quick Links</h5>
        <ul><li>Flight Booking Service</li><li>Hotel Booking Service</li><li>Ticket Booking Service</li><li>Torque League travel</li></ul>
      </div>
      <div class="col">
        <h5>Information</h5>
        <ul><li>About Kestrel Voyages</li><li>FAQ</li><li>Privacy Policy</li><li>Terms &amp; Conditions</li></ul>
      </div>
      <div class="col contact-col">
        <div class="brand"><span class="mark"></span>Kestrel Voyages Elite</div>
        <ul><li>+1 555 0199 271</li><li>support@kestrelvoyages.example</li><li>info@kestrelvoyages.example</li></ul>
      </div>
    </div>
  </div>
  <div class="chat">
    <svg width="24" height="20" viewBox="0 0 24 20" fill="none" stroke="#111" stroke-width="2"><path d="M12 2C6.5 2 2 5.3 2 9.3c0 2 1.1 3.8 2.9 5.1L4 18.5l4.6-2.3c1.1.3 2.2.4 3.4.4 5.5 0 10-3.3 10-7.3S17.5 2 12 2z"/></svg>
    Chat
  </div>
  <div class="legal">
    <div class="wrap"><span>Copyright 2025 Kestrel Voyages Elite</span><span>|</span><span>All Rights Reserved</span></div>
  </div>
</footer>

</body>
</html>
```